Google Form Graphic to suit our Brand and industry

Create a graphic / image for us to put at the top of our client enquiry google form.
The image will be a section of an architectural home with our branding over the top. Preferably translucent.
The image must suit the shape of the google forms image, which is an elongated rectangle
#003d5d - brand colour

Target Market(s)

residential home owners, high end architectural homes

Industry/Entity Type

Residential construction

Colors
0054AA
0677BA
7BADD7
CADEEF
E8F1F8

Requirements
Must have
• our branding and a photo of an architectural home in the background

```html
<!DOCTYPE html>
<html lang="en">
<head>
<meta charset="utf-8">
<title>Marlow Homes – Client Enquiry Header</title>
<link rel="stylesheet" href="https://fonts.googleapis.com/css2?family=Poppins:wght@500&display=swap">
<style>
  :root {
    --brand-navy: #003d5d;
    --sky-top: #2a3a4c;
    --sky-bottom: #1b2431;
    --interior-glow: #b57a44;
    --interior-deep: #5a3b22;
    --wordmark: #ffffff;
  }
  html, body {
    margin: 0;
    padding: 0;
    width: 1200px;
    height: 300px;
    overflow: hidden;
    background: var(--sky-bottom);
  }
  .banner {
    position: relative;
    width: 1200px;
    height: 300px;
    overflow: hidden;
  }
  .banner__photo {
    position: absolute;
    inset: 0;
    background:
      radial-gradient(ellipse 360px 120px at 760px 220px, var(--interior-glow) 0%, var(--interior-deep) 45%, rgba(90,59,34,0) 100%),
      radial-gradient(ellipse 220px 80px at 930px 230px, rgba(181,122,68,0.7) 0%, rgba(181,122,68,0) 100%),
      linear-gradient(180deg, var(--sky-top) 0%, var(--sky-bottom) 100%);
  }
  .banner__overlay {
    position: absolute;
    inset: 0;
  }
  .banner__name {
    position: absolute;
    left: 0;
    right: 0;
    top: 50%;
    transform: translateY(-50%);
    margin: 0;
    text-align: center;
    font-family: "Poppins", sans-serif;
    font-weight: 500;
    font-size: 74px;
    line-height: 1;
    letter-spacing: 8px;
    color: var(--wordmark);
    white-space: nowrap;
  }
</style>
</head>
<body>
  <div class="banner">
    <div class="banner__photo" role="img" aria-label="Photograph of a modern architectural home at dusk with warmly lit glass walls and a cantilevered upper level"></div>

    <svg class="banner__overlay" width="1200" height="300" viewBox="0 0 1200 300" aria-hidden="true">
      <path d="M0 0 H608 L528 88 Q500 122 526 160 L601 300 H0 Z" fill="var(--brand-navy)" fill-opacity="0.78"/>
    </svg>

    <h1 class="banner__name">MARLOW HOMES</h1>
  </div>
</body>
</html>
```